Packaging and labelling for Swiss made Organic CBD Oil

Visit our website www.velmarotiva.com
We have not put any product on yet as require packaging and label design .
Website will give you a great feel for the company and how we have used
the logo . The Drevask cbd product shown is a company similar to ourselves with similar core values , we liked the clean packaging design they have .

Im happy if you want use the mandala symbol in our logo separate from
VELMARO, to separate and use the mandala symbol as a larger icon than
it appears in our logo
Clean , Pure , organic feel. Like the product to look pharmaceutical and life changing not gimmicky.
Colours to go with or be the same as our logo colours
But not too cold and clinical
Bottle size 84mm x 25mm
Label size 75mm x 30mm
Box 30mm x 30mm x 100mm
6 products
Full Spectrum :
500mg CBD (5%)
1000mg CBD ( 10% )
1500mg CBD (15%)
2000mg CBD ( 20% )
Broad spectrum THC Free
500mg CBD (5%)
Pets
500mg Broad Spectrum THC Free
Updates

Would like the design to be more modern than traditional

LABEL Information Front of Bottle - Logo VELMARO & Mandala - Mandala can be used separately as design symbol Organic Cannabis Oil 1500mg CBD (15%) Ful Spectrum 10ml Back of bottle Ingredients: Organic Cannabis Oil Extract Organic Sunflower Seed Oil THC - 0.2% Certified Swiss Organic Cultivation Shake well before use. Store in a cool , dry place and out of the each of children BOX information Front and rear Logo - VELMARO & Mandala - Mandala can be used separately as a design symbol Organic Cannabis Oil 1500mg CBD (15%) Full Spectrum Sides x 2 This product is a food supplement and is not intended to diagnose, treat, cure or prevent any disease If you are pregnant, lactating or taking any medication consult your health care practitioner Suitable for vegetarians and vegans Ingredients Organic Cannabis Oil extract Organis Sunflower Oil Store in a cool ,dry place, out of the reach of children Recommended Use 1-5 drops ( 1 drop = 7.5mg CBD ) Subject to body weight and personal requirement - visit www.velmarotiva for more information 100% Natural 100% Organic GMO free 100% Vegan ( symbol with each ) Expiry date see bottle label Cultivated and manufactured in Switzerland

Target Market(s)

age 40 - 80

Font styles to use
Other font styles liked:
• In our website we have used Open Sans for the copy and Lato for headings .

Requirements
Must have
• look like an Industry leader
Velmaro will change the quality of peoples lives and in some cases may
even save lives so want look powerful and credible
Our Mission is - Through Delivering Pure , Premium , Organic products we will educate, inform and help people achieve healthier , happier lifestyles
Nice to have
• Colours to look good with our logo colours or be the same as our logo
colours
Logo Font - Avenir Black and Avenir Book

Font used in website - Content - Open Sans / Headings - Lato
If you have another font for the packaging information that will go well with
our logo, I'm happy for you to use your skills

```html
<!DOCTYPE html>
<html lang="en">
<head>
<meta charset="utf-8">
<title>Velmaro Organic Cannabis Oil – Front Label</title>
<link rel="stylesheet" href="https://fonts.googleapis.com/css2?family=Nunito+Sans:wght@300;400&display=swap">
<style>
  :root {
    --backdrop: #ecebef;
    --label-white: #ffffff;
    --ink-grey: #8d8d8f;
    --mark-teal: #8fd3d8;
    --pattern-light: #bfe6f1;
    --pattern-mid: #7cc2e6;
    --pattern-deep: #3f7fd0;
  }
  html, body {
    margin: 0;
    padding: 0;
    width: 1200px;
    height: 936px;
    overflow: hidden;
    background: var(--backdrop);
  }
  .canvas {
    position: relative;
    width: 1200px;
    height: 936px;
  }
  .front-label {
    position: absolute;
    left: 435px;
    top: 28px;
    width: 330px;
    height: 880px;
    background: var(--label-white);
    box-shadow: 0 2px 14px rgba(60, 50, 80, 0.12);
    font-family: "Nunito Sans", "Avenir", sans-serif;
    color: var(--ink-grey);
    overflow: hidden;
  }
  .brand-dot {
    position: absolute;
    left: 18px;
    top: 70px;
    width: 46px;
    height: 46px;
    border: 2px solid var(--mark-teal);
    border-radius: 50%;
    box-sizing: border-box;
  }
  .brand-name {
    position: absolute;
    left: 64px;
    top: 128px;
    margin: 0;
    font-size: 48px;
    font-weight: 400;
    letter-spacing: 1px;
    line-height: 1;
    color: var(--ink-grey);
  }
  .product-type {
    position: absolute;
    left: 0;
    right: 0;
    top: 240px;
    margin: 0;
    text-align: center;
    font-size: 28px;
    font-weight: 300;
    line-height: 1;
  }
  .strength {
    position: absolute;
    left: 0;
    right: 0;
    top: 458px;
    margin: 0;
    padding-right: 20px;
    text-align: center;
    font-size: 28px;
    font-weight: 300;
    line-height: 1;
  }
  .pattern-field {
    position: absolute;
    left: 0;
    right: 0;
    top: 515px;
    bottom: 0;
    border-radius: 120px 120px 0 0;
    background:
      radial-gradient(circle at 30% 75%, var(--pattern-light) 0%, transparent 55%),
      radial-gradient(circle at 78% 40%, var(--pattern-deep) 0%, transparent 60%),
      linear-gradient(160deg, var(--pattern-mid), var(--pattern-light));
    opacity: 0.75;
  }
</style>
</head>
<body>
  <main class="canvas">
    <section class="front-label">
      <span class="brand-dot" aria-hidden="true"></span>
      <h1 class="brand-name">VELMARO</h1>
      <p class="product-type">Organic Cannabis Oil</p>
      <p class="strength">1500mg</p>
      <div class="pattern-field" role="img" aria-label="Cluster of blue mandala circle ornaments filling the lower part of the label"></div>
    </section>
  </main>
</body>
</html>
```